Construction company that specializes in roofing and siding

https://havenridgeroofs.example/featured-projects/

https://www.pinecrestrenovationllc.example/#

https://www.ironmeadowhomes.example/residential-siding-services/

Please model a website after these examples
I posted a doc that has some content to get you started. I will upload more content and photos as the site progresses.

Coded - Design and coding required

5+ page

```html
<!DOCTYPE html>
<html lang="en">
<head>
<meta charset="utf-8">
<title>Granitepeak Construction – Roofing and Siding in Minnesota</title>
<link rel="stylesheet" href="https://fonts.googleapis.com/css2?family=Ubuntu:wght@400;500;700&family=Poppins:wght@400;500;600&display=swap">
<style>
:root{
  --ink:#222326;
  --slate:#55585c;
  --btn:#5b5d60;
  --muted:#8c8f93;
  --line:#b9bcc0;
  --paper:#ffffff;
  --mist:#eef0f2;
  --footer:#1f2124;
  --hero-a:#5d6b7a;
  --hero-b:#3f4a3c;
}
*{box-sizing:border-box;margin:0;padding:0}
html,body{width:1200px;height:4969px;overflow:hidden}
body{position:relative;background:var(--paper);font-family:"Poppins",sans-serif;color:var(--ink)}
.abs{position:absolute}
.ph{position:absolute;display:block}
.btn{position:absolute;background:var(--btn);color:#fff;font-family:"Poppins",sans-serif;font-weight:600;font-size:13px;letter-spacing:.5px;display:flex;align-items:center;justify-content:center;border-radius:3px;text-transform:uppercase}

/* header */
.site-header{position:absolute;left:0;top:0;width:1200px;height:154px;background:rgba(255,255,255,.9);z-index:5}
.brand{position:absolute;display:flex;align-items:center;gap:14px}
.brand-mark{width:56px;height:56px;background:var(--slate);border-radius:4px}
.brand-name{font-family:"Ubuntu",sans-serif;font-weight:700;font-size:25px;line-height:1.05;color:var(--slate);text-transform:uppercase;letter-spacing:1px}
.header-phone{left:652px;top:34px;display:flex;align-items:center;gap:14px;font-weight:600;font-size:18px}
.phone-dot{width:36px;height:36px;border-radius:50%;background:var(--slate);display:flex;align-items:center;justify-content:center}
.main-nav{left:494px;top:98px;width:561px;display:flex;justify-content:space-between;font-family:"Ubuntu",sans-serif;font-weight:500;font-size:15px;color:var(--slate)}

/* hero */
.hero{left:0;top:0;width:1200px;height:804px;background:linear-gradient(160deg,#7b8a98 0%,var(--hero-a) 35%,#4c5560 60%,var(--hero-b) 100%);clip-path:polygon(0 0,100% 0,100% 94%,0 100%)}
.hero-title{left:200px;top:418px;width:800px;text-align:center;font-family:"Ubuntu",sans-serif;font-weight:500;font-size:40px;line-height:56px;color:#fff}
.dots{left:575px;top:686px;display:flex;gap:7px}
.dots span{width:17px;height:17px;border-radius:50%;border:2px solid #fff}
.dots span.on{background:#fff}

/* about */
.about-bg{left:0;top:780px;width:1200px;height:640px;background:linear-gradient(180deg,#fff 0%,#f4efee 30%,#c8ccd0 60%,#8d9a86 88%,#6d8a55 100%)}
.about-veil{left:0;top:780px;width:1200px;height:640px;background:linear-gradient(90deg,rgba(255,255,255,.85) 0%,rgba(255,255,255,.4) 45%,rgba(255,255,255,.75) 100%)}
.about-heading{left:145px;top:880px;font-family:"Ubuntu",sans-serif;font-size:35px;line-height:48px;color:var(--ink);text-transform:uppercase}
.about-heading b{font-weight:500}
.rule{position:absolute;height:3px;background:var(--slate)}
.about-copy{left:612px;top:880px;width:445px;font-size:13.5px;line-height:24.5px;color:#333}
.about-copy p{margin-bottom:25px}

/* services */
.services-bg{left:0;top:1400px;width:1200px;height:860px;background:linear-gradient(180deg,#3a3d40 0%,#4d4f50 45%,#6b5e4a 80%,#4e5053 100%);clip-path:polygon(0 5%,100% 0,100% 100%,55% 95%,0 100%)}
.section-title{position:absolute;left:0;width:1200px;text-align:center;font-family:"Ubuntu",sans-serif;font-weight:700;font-size:38px;text-transform:uppercase}
.service-card{position:absolute;top:1665px;width:285px;height:413px;background:#fff}
.service-card .ph{left:0;top:0;width:285px;height:249px}
.service-card h3{position:absolute;top:272px;width:100%;text-align:center;font-weight:600;font-size:15px;letter-spacing:.5px}
.service-card p{position:absolute;top:300px;left:22px;width:241px;text-align:center;font-size:12.5px;line-height:21px;color:#444}
.service-card svg{position:absolute;left:132px;top:378px}

/* projects */
.proj-title{top:2328px;color:var(--ink)}
.proj-tag{left:501px;top:2795px;font-weight:600;font-size:15px;line-height:22px;color:#fff;text-transform:uppercase}
.proj-go{left:686px;top:2792px;width:42px;height:42px;border-radius:50%;background:rgba(80,82,86,.9);display:flex;align-items:center;justify-content:center}

/* testimonials */
.reviews-bg{left:0;top:3170px;width:1200px;height:685px;background:linear-gradient(180deg,#6d6f83 0%,#c98670 14%,#8b7378 26%,#4e5666 45%,#55605e 65%,#4f7a35 85%,#557a2c 100%);clip-path:polygon(0 0,100% 15%,100% 100%,0 93%)}
.review-box{left:305px;top:3428px;width:683px;height:262px;border:2px solid #fff}
.review-photo{left:212px;top:3453px;width:192px;height:192px;border-radius:50%;border:4px solid #fff;background:linear-gradient(160deg,#8b98a6,#5b6470 60%,#6e7a52)}
.review-text{left:496px;top:3470px;width:460px;color:#fff;font-size:16px;line-height:25px}
.review-name{left:496px;top:3608px;color:#fff;font-size:15px;font-weight:500}
.quote-mark{font-family:"Ubuntu",sans-serif;font-weight:700;font-size:86px;color:#fff;line-height:1}
.arrow-btn{width:30px;height:30px;border-radius:50%;border:2px solid rgba(255,255,255,.8);display:flex;align-items:center;justify-content:center}

/* subscribe + contact */
.h2-light{position:absolute;font-family:"Ubuntu",sans-serif;font-weight:500;font-size:38px;line-height:50px;color:var(--slate)}
.field{position:absolute;border:1.5px solid #b0b3b7;border-radius:3px;font-size:11.5px;color:#777;padding:0 10px;display:flex;align-items:center;justify-content:space-between;height:40px;background:#fff}
.contact-card{left:548px;top:3916px;width:507px;height:540px;background:#fff;z-index:2}

/* footer */
.footer{left:0;top:4398px;width:1200px;height:571px;background:linear-gradient(180deg,#2b2d30,var(--footer))}
.foot-h{position:absolute;color:#fff;font-weight:600;font-size:17px;text-transform:uppercase}
.foot-text{position:absolute;color:#e6e7e8;font-size:12.5px;line-height:21px}
.foot-list{position:absolute;list-style:none;color:#e6e7e8;font-size:12.5px;line-height:27px}
.contact-row{display:flex;gap:14px;align-items:flex-start;margin-bottom:10px}
.social{display:flex;gap:10px;margin-top:6px}
.social span{width:36px;height:36px;border-radius:50%;border:2px solid #fff}
.copyright{left:0;top:4896px;width:1200px;text-align:center;color:#fff;font-size:15px}
</style>
</head>
<body>

<!-- Hero -->
<div class="abs hero" role="img" aria-label="Aerial photo of a large stone house with a new grey shingle roof"></div>
<header class="site-header">
  <div class="brand" style="left:145px;top:36px">
    <span class="brand-mark"></span>
    <span class="brand-name">Granitepeak<br>Construction</span>
  </div>
  <div class="abs header-phone">
    <span class="phone-dot"><svg width="18" height="18" viewBox="0 0 24 24"><path fill="#fff" d="M6.6 10.8a15 15 0 0 0 6.6 6.6l2.2-2.2a1 1 0 0 1 1-.25 11.4 11.4 0 0 0 3.6.57 1 1 0 0 1 1 1V20a1 1 0 0 1-1 1A17 17 0 0 1 3 4a1 1 0 0 1 1-1h3.5a1 1 0 0 1 1 1c0 1.25.2 2.45.57 3.57a1 1 0 0 1-.25 1z"/></svg></span>
    +12 555 0142
  </div>
  <div class="btn" style="left:870px;top:31px;width:185px;height:40px">Request a Quote</div>
  <nav class="abs main-nav"><span>HOME</span><span>ABOUT US</span><span>SERVICES</span><span>NEWS</span><span>LOCATION</span><span>CONTACT</span></nav>
</header>
<h1 class="abs hero-title">Granitepeak Construction is<br>your source for roofing and siding<br>in Minnesota.</h1>
<div class="btn" style="left:525px;top:598px;width:150px;height:39px">Learn More</div>
<div class="abs dots"><span class="on"></span><span></span><span></span></div>

<!-- About -->
<div class="abs about-bg" role="img" aria-label="Faded photo of a modern grey-sided house with a stone base and lawn"></div>
<div class="abs about-veil"></div>
<div class="abs about-bg" style="z-index:-1"></div>
<div class="abs" style="left:0;top:780px;width:1200px;height:30px;background:#fff;clip-path:polygon(0 0,100% 0,100% 0,0 100%)"></div>
<h2 class="abs about-heading">About Us<br><b>Granitepeak<br>Construction</b></h2>
<div class="rule" style="left:145px;top:1049px;width:75px"></div>
<div class="abs about-copy">
  <p>In 2016 Tom Hale started helping people with their home improvement projects. His very first job was installing window trim for a wonderful homeowner in Forest lake MN. He did his best work and made sure he treated his first customer like family. Afterall, his first customer was Rita Hale, his Mom.</p>
  <p>Today, Tom and the Granitepeak Construction team are helping homeowners around Minnesota; carrying the spirit of his first job onto every job they touch.</p>
  <p>"We are helping a lot more people now, but we haven't lost the dedication to service and craftsmanship that I had on my very first job."</p>
</div>
<div class="btn" style="left:612px;top:1221px;width:152px;height:39px">Learn More</div>

<!-- Services -->
<div class="abs services-bg" role="img" aria-label="Dark aerial photo of a roof under construction with work vehicles"></div>
<h2 class="section-title" style="top:1550px;color:#fff">Our Services</h2>
<div class="rule" style="left:532px;top:1617px;width:136px;background:#fff"></div>

<article class="service-card" style="left:145px">
  <div class="ph" role="img" aria-label="Roofers laying dark shingles on battens" style="background:linear-gradient(160deg,#a88a62 0%,#6b5a47 35%,#3a3d42 60%,#2c2f33 100%)"></div>
  <h3>ROOFING</h3>
  <p>Sed ut perspiciatis unde omnis iste natus sit voluptatem accusantium doloremque laudantium</p>
  <svg width="22" height="12" viewBox="0 0 22 12"><path d="M0 6h20M15 1l5 5-5 5" stroke="#333" stroke-width="2" fill="none"/></svg>
</article>
<article class="service-card" style="left:457px">
  <div class="ph" role="img" aria-label="White house siding and gutter against a sunset sky" style="background:linear-gradient(170deg,#5f7fa8 0%,#d48a8a 35%,#7d858f 60%,#d9dcdf 100%)"></div>
  <h3>SIDING</h3>
  <p>Sed ut perspiciatis unde omnis iste natus sit voluptatem accusantium doloremque laudantium</p>
  <svg width="22" height="12" viewBox="0 0 22 12"><path d="M0 6h20M15 1l5 5-5 5" stroke="#333" stroke-width="2" fill="none"/></svg>
</article>
<article class="service-card" style="left:771px">
  <div class="ph" role="img" aria-label="Black gutter and downspout under a tiled roof edge" style="background:linear-gradient(170deg,#4f86c8 0%,#8db4de 30%,#2d3035 55%,#e6dfd2 100%)"></div>
  <h3>GUTTERS</h3>
  <p>Sed ut perspiciatis unde omnis iste natus sit voluptatem accusantium doloremque laudantium</p>
  <svg width="22" height="12" viewBox="0 0 22 12"><path d="M0 6h20M15 1l5 5-5 5" stroke="#333" stroke-width="2" fill="none"/></svg>
</article>

<!-- Projects -->
<h2 class="section-title proj-title">Our Projects</h2>
<div class="rule" style="left:532px;top:2397px;width:136px"></div>
<div class="ph" role="img" aria-label="Grey shingle roof over a white stucco house" style="left:145px;top:2442px;width:283px;height:318px;background:linear-gradient(160deg,#3f6b2f,#8a9098 40%,#d9d6cf)"></div>
<div class="ph" role="img" aria-label="Dark roof gables of a beige house under blue sky" style="left:438px;top:2442px;width:324px;height:318px;background:linear-gradient(180deg,#3f78c4 0%,#6f9bd4 45%,#4a4d52 70%,#cfc4b0 100%)"></div>
<div class="ph" role="img" aria-label="Close-up of a brown shingle roof" style="left:772px;top:2442px;width:283px;height:318px;background:linear-gradient(150deg,#40512e,#7a6a5a 30%,#8b7b6c 70%,#6d5f52)"></div>
<div class="ph" role="img" aria-label="House with a new dark roof and chimney among green hills" style="left:145px;top:2770px;width:617px;height:316px;background:linear-gradient(180deg,#9fb2c8 0%,#7d95a5 25%,#4f5258 50%,#5d7c34 85%,#6f9a2a 100%)"></div>
<div class="abs proj-tag">Lakeside Reroof<br>Sed ut perspiciatis</div>
<div class="abs proj-go"><svg width="18" height="12" viewBox="0 0 22 12"><path d="M0 6h20M15 1l5 5-5 5" stroke="#fff" stroke-width="2" fill="none"/></svg></div>
<div class="ph" role="img" aria-label="Stone house with a grey shingle roof and timber porch" style="left:772px;top:2770px;width:283px;height:316px;background:linear-gradient(160deg,#4e5868,#6b7078 45%,#5b6a45 80%,#6e8a3e)"></div>

<!-- Testimonials -->
<div class="abs reviews-bg" role="img" aria-label="Modern house with grey siding and lawn under a pink sunset sky"></div>
<h2 class="section-title" style="top:3308px;color:#fff">What Others Are Saying</h2>
<div class="rule" style="left:545px;top:3373px;width:110px;background:#fff"></div>
<div class="abs review-box"></div>
<div class="abs review-photo" role="img" aria-label="Couple seen from behind looking at their house"></div>
<div class="abs quote-mark" style="left:436px;top:3448px">&ldquo;</div>
<p class="abs review-text">Sed ut perspiciatis unde omnis iste natus error sit voluptatem accusantium doloremque laudantium, totam rem aperiam, eaque ipsa quae ab illo inventore veritatis et quasi architecto beatae vitae dicta sunt explicabo. Nemo enim ipsam voluptatem quia voluptas</p>
<div class="abs review-name">Mark Ellison - Northfield Homes</div>
<svg class="abs" style="left:496px;top:3640px" width="80" height="14" viewBox="0 0 80 14">
  <g fill="#fff"><path id="st" d="M7 0l2 5h5l-4 3 1.6 5L7 10 2.4 13 4 8 0 5h5z"/><use href="#st" x="16"/><use href="#st" x="32"/><use href="#st" x="48"/><use href="#st" x="64"/></g>
</svg>
<div class="abs quote-mark" style="left:862px;top:3594px">&rdquo;</div>
<div class="abs arrow-btn" style="left:132px;top:3540px"><svg width="10" height="10" viewBox="0 0 10 10"><path d="M7 1L3 5l4 4" stroke="#fff" stroke-width="1.6" fill="none"/></svg></div>
<div class="abs arrow-btn" style="left:1037px;top:3540px"><svg width="10" height="10" viewBox="0 0 10 10"><path d="M3 1l4 4-4 4" stroke="#fff" stroke-width="1.6" fill="none"/></svg></div>

<!-- Subscribe -->
<h2 class="h2-light" style="left:145px;top:3946px">Subscribe<br>our newsletter</h2>
<div class="field" style="left:145px;top:4086px;width:371px;height:52px;border-width:2px;border-color:#666;padding-left:28px;color:#444;font-size:12px">Email Address</div>
<div class="btn" style="left:145px;top:4159px;width:142px;height:41px;text-transform:none;font-size:12px">Submit Now</div>

<!-- Footer -->
<footer class="abs footer" role="img" aria-label="Dark aerial photo of a house roof"></footer>
<div class="brand" style="left:145px;top:4528px">
  <span class="brand-mark" style="background:#8a8d91"></span>
  <span class="brand-name" style="color:#b8babd">Granitepeak<br>Construction</span>
</div>
<p class="foot-text" style="left:142px;top:4626px;width:360px">Sed ut perspiciatis unde omnis iste natus error sit voluptatem accusantium doloremque laudantium, totam rem aperiam, eaque ipsa quae ab illo inventore veritatis et quasi architecto beatae vitae dicta sunt explicabo. Nemo enim ipsam voluptatem quia voluptas sit aspernatur aut odit aut fugit, sed quia consequuntur magni dolores eos qui ratione</p>

<h3 class="foot-h" style="left:579px;top:4514px">Contact Us</h3>
<div class="foot-text" style="left:579px;top:4566px;width:330px">
  <div class="contact-row"><svg width="16" height="18" viewBox="0 0 16 18"><path d="M8 1a6 6 0 0 0-6 6c0 4.5 6 10 6 10s6-5.5 6-10a6 6 0 0 0-6-6z" stroke="#fff" stroke-width="1.5" fill="none"/><circle cx="8" cy="7" r="2" stroke="#fff" stroke-width="1.5" fill="none"/></svg><span>6021 enim ipsam voluptatem<br>quia voluptas</span></div>
  <div class="contact-row"><svg width="16" height="16" viewBox="0 0 24 24"><path d="M6.6 10.8a15 15 0 0 0 6.6 6.6l2.2-2.2 4.6 1V20A17 17 0 0 1 3 4h4.5l1 4.6z" stroke="#fff" stroke-width="1.8" fill="none"/></svg><span>Phone: 12 555 0142</span></div>
  <div class="contact-row"><svg width="16" height="16" viewBox="0 0 16 16"><rect x="1" y="5" width="14" height="9" fill="#fff"/><rect x="4" y="1" width="8" height="5" fill="#fff"/></svg><span>Fax: 12 555 0143</span></div>
  <div class="contact-row"><svg width="16" height="14" viewBox="0 0 16 14"><rect x="1" y="2" width="14" height="10" stroke="#fff" stroke-width="1.4" fill="none"/><path d="M1 2l7 6 7-6" stroke="#fff" stroke-width="1.4" fill="none"/></svg><span>Email: hello@granitepeakbuild.example</span></div>
  <div class="social"><span></span><span></span><span></span></div>
</div>

<h3 class="foot-h" style="left:936px;top:4514px">Quick Links</h3>
<ul class="foot-list" style="left:936px;top:4560px"><li>Home</li><li>About us</li><li>Services</li><li>News</li><li>Location</li><li>Contact</li></ul>
<div class="abs" style="left:0;top:4851px;width:1200px;height:1px;background:rgba(255,255,255,.2)"></div>
<div class="abs copyright">Granitepeak Construction (c) 2024 | All Rights Reserved</div>

<!-- Contact form card -->
<section class="abs contact-card">
  <h2 class="h2-light" style="left:35px;top:22px">Contact Us</h2>
  <p class="abs" style="left:35px;top:80px;width:440px;font-size:11px;line-height:20px;color:#888">Enter your contact details below and a customer success specialists will reach out to you next business day.</p>
  <div class="field" style="left:35px;top:135px;width:212px">First Name *</div>
  <div class="field" style="left:260px;top:135px;width:214px">Last Name *</div>
  <div class="field" style="left:35px;top:189px;width:212px">Email *</div>
  <div class="field" style="left:260px;top:189px;width:214px">Phone *</div>
  <div class="field" style="left:35px;top:243px;width:212px">Location *<svg width="9" height="6" viewBox="0 0 9 6"><path d="M0 0h9L4.5 6z" fill="#555"/></svg></div>
  <div class="field" style="left:260px;top:243px;width:214px">What you Need? *<svg width="9" height="6" viewBox="0 0 9 6"><path d="M0 0h9L4.5 6z" fill="#555"/></svg></div>
  <div class="field" style="left:35px;top:299px;width:439px;height:118px;align-items:flex-start;padding-top:12px">How can we help? *</div>
  <div class="btn" style="left:310px;top:440px;width:162px;height:46px;text-transform:none;font-size:13px">Send Message</div>
</section>

</body>
</html>
```